Our Velvetline

I am developing a web site which sells preowned high end designer handbags and accessories. Some of the brands include: Corvane, Edmond Sarrelle & Velsa, to name a few. I am after a luxurious and high end feel.

Some brands I like that express this feel include: Astrel, Velsa, tinclosetly.com, purseswaporkeep.com

I am after a logo, business card, letterhead, with compliments, address label and envelope designs.
The business name is Our velvetline, and the website will be www.ourvelvetline.com.au. I have thoughts of using OVL as a logo or OUR velvetline.com.au

I don't want a large logo, it needs to blend in with the name in some way - or may not need an image at all, if the style of the font speaks to the brand.

Thank-you

Project Deadline Extended
Reason: I would like to give designers plenty of time to be able to submit a design.

Target Market(s)

Women, aged 25-60 who are into fashion

Industry/Entity Type

Business

Requirements
Must have
• High End
Luxurious

```html
<!DOCTYPE html>
<html lang="en">
<head>
<meta charset="utf-8">
<title>Our Velvetline — Stationery Set</title>
<link href="https://fonts.googleapis.com/css2?family=EB+Garamond:wght@400&display=swap" rel="stylesheet">
<style>
  :root {
    --stage-outer: #8f8f91;
    --stage-inner: #e2e2e3;
    --ink-deep: #2c2c2e;
    --ink-band: #3b3b3d;
    --ink-slate: #48484a;
    --ink-strip: #6e6e70;
    --ink-text: #3a3a3a;
    --ink-soft: #8a8a8c;
    --ink-pale: #b9b9bb;
    --paper: #ffffff;
    --paper-cool: #f1f1f3;
    --shadow: 2px 3px 6px rgba(0,0,0,.35);
    --serif: "EB Garamond", Georgia, serif;
  }
  * { box-sizing: border-box; margin: 0; padding: 0; }
  html, body { width: 1200px; height: 800px; overflow: hidden; }
  body { font-family: var(--serif); background: var(--stage-outer); }
  .stage {
    position: relative; width: 1200px; height: 800px;
    background: radial-gradient(ellipse at 50% 45%, #f4f4f5 0%, #d0d0d2 60%, #a2a2a4 100%);
  }
  .stage-frame {
    position: absolute; left: 30px; top: 22px; width: 1138px; height: 756px;
    background: radial-gradient(ellipse at 50% 40%, #fafafa 0%, var(--stage-inner) 55%, #b4b4b6 100%);
  }
  .piece { position: absolute; box-shadow: var(--shadow); overflow: hidden; }
  .pattern-band { position: absolute; left: 0; right: 0; background: var(--ink-band); }

  /* brand lockup */
  .brand-name { color: var(--ink-soft); line-height: 1; white-space: nowrap; }
  .brand-tagline { color: var(--ink-text); line-height: 1.1; white-space: nowrap; }
  .brand-url { color: var(--ink-text); line-height: 1.1; white-space: nowrap; }

  .hero-brand { position: absolute; left: 36px; top: 40px; }
  .hero-brand .brand-name { font-size: 52px; }
  .hero-brand .brand-tagline { font-size: 21px; margin-top: 22px; color: var(--ink-soft); }
  .hero-brand .brand-url { font-size: 12px; margin-left: 32px; }

  .small-brand .brand-name { font-size: 22px; }
  .small-brand .brand-tagline { font-size: 10px; margin-top: 6px; }
  .small-brand .brand-url { font-size: 6px; margin-left: 16px; }

  .address-line { position: absolute; font-size: 8px; color: var(--ink-text); white-space: nowrap; }

  /* letterhead */
  .letterhead { left: 312px; top: 80px; width: 443px; height: 623px; background: var(--paper); }
  .letterhead .small-brand { position: absolute; left: 10px; top: 28px; }

  /* compliments slip */
  .compliments { left: 670px; top: 177px; width: 452px; height: 214px; background: var(--paper); }
  .compliments .head { position: absolute; left: 0; top: 0; right: 0; height: 75px; background: var(--ink-slate); }
  .compliments .strip { position: absolute; left: 0; top: 75px; right: 0; height: 11px; background: var(--ink-strip); }
  .compliments .small-brand { position: absolute; left: 32px; top: 18px; }
  .compliments .small-brand .brand-name { color: var(--ink-pale); }
  .compliments .small-brand .brand-tagline,
  .compliments .small-brand .brand-url { color: var(--ink-pale); }
  .staff-name { position: absolute; font-size: 10px; color: var(--ink-pale); white-space: nowrap; }
  .staff-role { position: absolute; font-size: 7px; color: var(--ink-pale); white-space: nowrap; }
  .with-compliments { position: absolute; right: 14px; top: 158px; font-size: 14px; color: var(--ink-deep); }

  /* envelopes */
  .envelope-back { left: 515px; top: 424px; width: 473px; height: 224px; background: var(--paper-cool); }
  .envelope-front { left: 670px; top: 510px; width: 473px; height: 226px; background: var(--paper-cool); }
  .envelope-front .small-brand { position: absolute; left: 12px; top: 30px; }

  /* business cards */
  .card { width: 250px; height: 122px; }
  .card-back { left: 108px; top: 230px; background: var(--ink-deep); transform: rotate(-10.8deg); }
  .card-back .card-pattern { position: absolute; inset: 0; background: #262628; }
  .card-back .small-brand { position: absolute; left: 112px; top: 40px; }
  .card-back .small-brand .brand-name { color: #9a9a9c; font-size: 24px; }
  .card-back .small-brand .brand-tagline,
  .card-back .small-brand .brand-url { color: var(--ink-pale); }
  .card-front { left: 248px; top: 319px; background: var(--paper); transform: rotate(-16deg); }
  .card-front .head { position: absolute; left: 0; top: 0; right: 0; height: 54px; background: var(--ink-slate); }
  .card-front .strip { position: absolute; left: 0; top: 54px; right: 0; height: 10px; background: var(--ink-strip); }
  .card-front .contact { position: absolute; left: 12px; top: 80px; font-size: 8px; color: var(--ink-soft); line-height: 1.5; }

  /* address label */
  .address-label { left: 163px; top: 510px; width: 234px; height: 130px; background: var(--ink-slate); }
  .address-label .card-pattern { position: absolute; inset: 0; background: var(--ink-slate); }
  .address-label .label-panel {
    position: absolute; left: 23px; top: 20px; width: 189px; height: 85px;
    background: var(--paper); text-align: center; color: var(--ink-text);
  }
  .label-panel .recipient { font-size: 13px; margin-top: 6px; }
  .label-panel .lines { font-size: 9px; line-height: 1.3; margin-top: 4px; }
</style>
</head>
<body>
<main class="stage">
  <div class="stage-frame"></div>

  <header class="hero-brand">
    <div class="brand-name">Our Velvetline</div>
    <div class="brand-tagline">High and Luxurious</div>
    <div class="brand-url">www.ourvelvetline.com.au</div>
  </header>

  <!-- letterhead -->
  <section class="piece letterhead">
    <div class="pattern-band" style="top:0;height:18px" role="img" aria-label="Repeating brand lettering pattern band"></div>
    <div class="small-brand">
      <div class="brand-name">Our Velvetline</div>
      <div class="brand-tagline">High and Luxurious</div>
      <div class="brand-url">www.ourvelvetline.com.au</div>
    </div>
    <div class="address-line" style="left:74px;top:593px">Number street, suburb, post code, city, state. p: 402 118 956 &nbsp;e: info@ourvelvetline.com.au</div>
    <div class="pattern-band" style="bottom:0;height:20px" role="img" aria-label="Repeating brand lettering pattern band"></div>
  </section>

  <!-- compliments slip -->
  <section class="piece compliments">
    <div class="head"></div>
    <div class="strip"></div>
    <div class="small-brand">
      <div class="brand-name">Our Velvetline</div>
      <div class="brand-tagline">High and Luxurious</div>
      <div class="brand-url">www.ourvelvetline.com.au</div>
    </div>
    <div class="staff-name" style="right:32px;top:76px">Marisa Holt</div>
    <div class="staff-role" style="right:42px;top:88px">Sells manager</div>
    <div class="with-compliments">With Compliments</div>
    <div class="address-line" style="left:80px;top:183px">Number street, suburb, post code, city, state. p: 402 118 956 &nbsp;e: info@ourvelvetline.com.au</div>
    <div class="pattern-band" style="bottom:0;height:18px" role="img" aria-label="Repeating brand lettering pattern band"></div>
  </section>

  <!-- envelope back -->
  <section class="piece envelope-back">
    <svg width="473" height="224" style="position:absolute;left:0;top:0" aria-hidden="true">
      <polygon points="0,0 473,0 285,86" fill="#2c2c2e"/>
    </svg>
    <div class="pattern-band" style="bottom:0;height:20px" role="img" aria-label="Repeating brand lettering pattern band"></div>
  </section>

  <!-- envelope front -->
  <section class="piece envelope-front">
    <div class="pattern-band" style="top:0;height:20px" role="img" aria-label="Repeating brand lettering pattern band"></div>
    <div class="small-brand">
      <div class="brand-name">Our Velvetline</div>
      <div class="brand-tagline">High and Luxurious</div>
      <div class="brand-url">www.ourvelvetline.com.au</div>
    </div>
    <div class="address-line" style="left:80px;top:193px;color:var(--ink-soft)">Number street, suburb, post code, city, state. p: 402 118 956 &nbsp;e: info@ourvelvetline.com.au</div>
    <div class="pattern-band" style="bottom:0;height:18px" role="img" aria-label="Repeating brand lettering pattern band"></div>
  </section>

  <!-- business card back -->
  <section class="piece card card-back">
    <div class="card-pattern" role="img" aria-label="Faint repeating brand lettering pattern"></div>
    <div class="small-brand">
      <div class="brand-name">Our Velvetline</div>
      <div class="brand-tagline">High and Luxurious</div>
      <div class="brand-url">www.ourvelvetline.com.au</div>
    </div>
  </section>

  <!-- business card front -->
  <section class="piece card card-front">
    <div class="head" role="img" aria-label="Dark band with faint brand lettering pattern"></div>
    <div class="strip"></div>
    <div class="staff-name" style="right:14px;top:52px;font-size:11px">Marisa Holt</div>
    <div class="staff-role" style="right:26px;top:66px;color:var(--ink-soft)">Sells manager</div>
    <div class="contact">p: 402 118 956<br>e: info@ourvelvetline.com.au</div>
  </section>

  <!-- address label -->
  <section class="piece address-label">
    <div class="card-pattern" role="img" aria-label="Repeating brand lettering pattern"></div>
    <div class="label-panel">
      <div class="recipient">Clara Benning</div>
      <div class="lines">Number street, suburb, post code,<br>city, state.<br>p: 402 118 956<br>e: info@ourvelvetline.com.au</div>
    </div>
  </section>
</main>
</body>
</html>
```